Business Cards for new orthopaedic surgery practice

My husband and I are starting our own orthopaedic surgery practice. We are looking for a business card that is uniform, but one will have my name/title and the other will have his. You can just create one design with my name on it for now. But when I choose your design as the winning design I will ask that you add another copy with his name/title.

We are looking for classy, simple, elite all in one. We like dark blues/a little gold/yellow. Something that goes with our logo. We want our logo incorporated. Here is all the info you need:
Business name: RV Spine & Vitality Center
Location: 38915 North Bramble Ave
Maple Harbor, FL 33490
Phone: 954-218-4630
Fax: 954-571-2846
Email: info@myrvspine.example

Names: Lucinda Ferrow, M.D.
Board Certified Hand and Upper Extremity Surgeon

Emeka Dlunga, M.D.
Board Certified Hip & Knee Replacement/General Orthopaedic Surgeon

Can decide what you want to put on the back. Maybe a slogan:
Grounded in Skill. Devoted to You

I am just going to upload our logo. The only thing is if we select you as the winning design, the location, and phone numbers may change. We will need your help to update that once fully solidified.

Industry/Entity Type

Medical

Contact Information for Business Card

Colors
0054AA
0677BA
7BADD7
CADEEF
E8F1F8
0094D4
00A9DD
6FCCEA
C7EBF8
E9F6FB

Requirements
Must have
• class, appeal,
Should not have
• We want to air on the side of masculine if we are looking at masculine vs. feminine feel. But we still want it classy, sophisticated, and something we will love

```html
<!DOCTYPE html>
<html lang="en">
<head>
<meta charset="utf-8">
<title>RV Spine &amp; Vitality Center – Business Card</title>
<link rel="stylesheet" href="https://fonts.googleapis.com/css2?family=Poppins:wght@500;600;700&family=Source+Sans+3:wght@400&display=swap">
<style>
  :root {
    --navy: #1b2a4e;
    --gold: #c9a25e;
    --gold-mid: #bf955a;
    --gold-dark: #b08440;
    --ink: #6b6b6b;
    --paper: #ffffff;
    --backdrop: #e1e2e4;
  }
  * { margin: 0; padding: 0; box-sizing: border-box; }
  html, body { width: 1200px; height: 528px; overflow: hidden; background: var(--backdrop); }
  .stage { position: relative; width: 1200px; height: 528px; }
  .card { position: absolute; top: 121px; width: 479px; height: 287px; overflow: hidden; }
  .card--front { left: 96px; background: var(--paper); }
  .card--back { left: 625px; background: var(--navy); }
  .card__band { position: absolute; left: 0; top: 0; width: 479px; height: 287px; }
  .card--back .card__band { transform: scaleX(-1); }

  .brand-mark {
    position: absolute; width: 150px; text-align: center;
    font-family: "Poppins", sans-serif; font-weight: 600;
    font-size: 15px; line-height: 1.3; letter-spacing: 0.02em;
  }
  .card--front .brand-mark { left: 55px; top: 118px; color: var(--navy); }
  .card--back .brand-mark { left: 164px; top: 108px; color: var(--paper); }

  .person { position: absolute; left: 248px; top: 60px; }
  .person__name { font-family: "Poppins", sans-serif; font-weight: 700; font-size: 19px; color: var(--navy); line-height: 1.1; white-space: nowrap; }
  .person__title { font-weight: 500; }
  .person__role { font-family: "Source Sans 3", sans-serif; font-size: 10px; color: var(--ink); margin-top: 2px; }
  .person__rule { width: 41px; height: 1.5px; background: var(--ink); margin-top: 6px; }

  .contacts { position: absolute; left: 248px; top: 113px; list-style: none; font-family: "Source Sans 3", sans-serif; font-size: 12.5px; color: var(--ink); }
  .contact { position: relative; padding-left: 18px; line-height: 13.5px; white-space: nowrap; }
  .contact--address { margin-bottom: 12px; }
  .contact + .contact { margin-top: 9px; }
  .contact--address + .contact { margin-top: 0; }
  .contact__icon { position: absolute; left: 0; top: 0; width: 14px; height: 14px; }

  .slogan { position: absolute; left: 0; width: 479px; top: 210px; text-align: center; font-family: "Poppins", sans-serif; font-weight: 500; font-size: 15px; color: var(--paper); }
</style>
</head>
<body>
<main class="stage">

  <section class="card card--front" aria-label="Business card front">
    <svg class="card__band" viewBox="0 0 479 287" aria-hidden="true">
      <polygon points="0,253.5 95,253.5 108,274 479,274 479,287 0,287" fill="var(--navy)"/>
      <polygon points="95,253.5 145,253.5 157,269 107,269" fill="var(--gold-dark)"/>
      <polygon points="145,253.5 195,253.5 207,269 157,269" fill="var(--gold-mid)"/>
      <polygon points="195,253.5 252,253.5 262,269 207,269" fill="var(--gold)"/>
      <rect x="269" y="260.5" width="198" height="2" fill="var(--gold)"/>
    </svg>

    <div class="brand-mark">RV Spine &amp;<br>Vitality Center</div>

    <div class="person">
      <h1 class="person__name">Lucinda Ferrow, <span class="person__title">M.D.</span></h1>
      <p class="person__role">Hand and Upper Extremity Surgery</p>
      <div class="person__rule"></div>
    </div>

    <ul class="contacts">
      <li class="contact contact--address">
        <svg class="contact__icon" viewBox="0 0 14 14" aria-hidden="true">
          <rect width="14" height="14" rx="1.5" fill="var(--navy)"/>
          <path d="M7 2.6a3 3 0 0 0-3 3c0 2.2 3 5.8 3 5.8s3-3.6 3-5.8a3 3 0 0 0-3-3z" fill="#fff"/>
          <circle cx="7" cy="5.6" r="1.2" fill="var(--navy)"/>
        </svg>
        38915 North Bramble Ave<br>Maple Harbor, FL 33490
      </li>
      <li class="contact contact--phone">
        <svg class="contact__icon" viewBox="0 0 14 14" aria-hidden="true">
          <rect width="14" height="14" rx="1.5" fill="var(--gold)"/>
          <path d="M4.4 3l1.5 0.2 0.7 2-1 0.8a6 6 0 0 0 2.5 2.5l0.8-1 2 0.7 0.2 1.5-1.2 1.1C7 10.6 3.4 7 3.3 4.2z" fill="#fff"/>
        </svg>
        954-218-4630
      </li>
      <li class="contact contact--fax">
        <svg class="contact__icon" viewBox="0 0 14 14" aria-hidden="true">
          <rect width="14" height="14" rx="1.5" fill="var(--gold)"/>
          <rect x="4.5" y="2.8" width="5" height="2.4" fill="#fff"/>
          <rect x="3" y="5.6" width="8" height="4" rx="0.6" fill="#fff"/>
          <rect x="4.5" y="8.4" width="5" height="2.8" fill="#fff" stroke="var(--gold)" stroke-width="0.6"/>
        </svg>
        954-571-2846
      </li>
      <li class="contact contact--email">
        <svg class="contact__icon" viewBox="0 0 14 14" aria-hidden="true">
          <rect width="14" height="14" rx="1.5" fill="var(--gold)"/>
          <rect x="2.6" y="4" width="8.8" height="6" fill="none" stroke="#fff" stroke-width="1"/>
          <path d="M2.8 4.2L7 7.6l4.2-3.4M2.8 9.8l3-2.6M11.2 9.8l-3-2.6" fill="none" stroke="#fff" stroke-width="0.9"/>
        </svg>
        info@myrvspine.example
      </li>
    </ul>
  </section>

  <section class="card card--back" aria-label="Business card back">
    <svg class="card__band" viewBox="0 0 479 287" aria-hidden="true">
      <polygon points="0,253.5 95,253.5 108,274 479,274 479,287 0,287" fill="var(--paper)"/>
      <polygon points="95,253.5 145,253.5 157,269 107,269" fill="var(--gold-dark)"/>
      <polygon points="145,253.5 195,253.5 207,269 157,269" fill="var(--gold-mid)"/>
      <polygon points="195,253.5 252,253.5 262,269 207,269" fill="var(--gold)"/>
      <rect x="269" y="260.5" width="198" height="2" fill="var(--gold)"/>
    </svg>

    <div class="brand-mark">RV Spine &amp;<br>Vitality Center</div>

    <p class="slogan">Grounded in Skill. Devoted to You</p>
  </section>

</main>
</body>
</html>
```